Business Card Design needed for start up company Pramora

In need of a new business card designed for a start up company based in Sydney, Pramora is a new start up innovative Company, our mission it to make property accessible for everyday Australian and to become the leading Real Estate platform in Australia. We want it to be fresh and clean.

Industry/Entity Type

Financial

Contact Information for Business Card

Section for Name
Section for Title

PRAMORA - Where Doors Open Wide
Mobile:
Direct:

Font styles to use
Sans Serif

Colors
33a6d7
0692cd
0255a3
ffffff

Requirements
Must have
• Logo, all business card details

```html
<!DOCTYPE html>
<html lang="en">
<head>
<meta charset="utf-8">
<title>Pramora Business Card</title>
<link href="https://fonts.googleapis.com/css2?family=Roboto+Condensed:wght@400;700&display=swap" rel="stylesheet">
<style>
  :root {
    --sky: #33a6d7;
    --azure: #0692cd;
    --navy: #0255a3;
    --white: #ffffff;
    --ink: #1b1b1b;
    --stage: #e7e9ec;
  }
  * { box-sizing: border-box; margin: 0; padding: 0; }
  html, body { width: 1200px; height: 1200px; overflow: hidden; }
  body {
    background: var(--stage);
    font-family: "Roboto Condensed", Arial, sans-serif;
    position: relative;
  }
  .card {
    position: absolute;
    left: 150px;
    width: 900px;
    height: 514px;
    background: var(--white);
    overflow: hidden;
    box-shadow: 0 6px 22px rgba(0,0,0,0.18);
  }
  .card--front { top: 56px; }
  .card--back { top: 630px; }

  .stripe { position: absolute; height: 16px; }
  .stripe--a { top: 150px; left: 0; width: 470px; background: var(--azure); }
  .stripe--b { top: 196px; left: 30px; width: 320px; background: var(--navy); }
  .stripe--c { top: 300px; left: 620px; width: 280px; background: var(--sky); }
  .stripe--d { top: 346px; left: 470px; width: 360px; background: var(--azure); }

  .brand {
    position: absolute;
    top: 50%; left: 50%;
    transform: translate(-50%, -50%);
    display: flex; align-items: center; gap: 18px;
  }
  .brand__dot {
    width: 96px; height: 96px; border-radius: 50%;
    background: var(--azure);
  }
  .brand__name {
    font-weight: 700; font-size: 96px; letter-spacing: 2px;
    color: var(--navy); line-height: 1;
  }

  .identity {
    position: absolute; left: 120px; top: 190px; color: var(--ink);
  }
  .identity__title { font-size: 46px; line-height: 1; }
  .identity__company { font-size: 32px; margin-top: 14px; }

  .timeline { position: absolute; inset: 0; }
  .contact {
    position: absolute; font-size: 17px; color: var(--ink); white-space: nowrap;
  }
  .wave { position: absolute; inset: 0; }
</style>
</head>
<body>

<section class="card card--front" aria-label="Card front">
  <div class="stripe stripe--a"></div>
  <div class="stripe stripe--b"></div>
  <div class="stripe stripe--c"></div>
  <div class="stripe stripe--d"></div>
  <div class="brand">
    <span class="brand__dot"></span>
    <span class="brand__name">PRAMORA</span>
  </div>
</section>

<section class="card card--back" aria-label="Card back">
  <svg class="wave" viewBox="0 0 900 514" aria-hidden="true">
    <defs>
      <linearGradient id="waveFill" x1="0" y1="1" x2="1" y2="0">
        <stop offset="0" stop-color="#0692cd"/>
        <stop offset="1" stop-color="#33a6d7"/>
      </linearGradient>
    </defs>
    <path d="M200 514 C225 420 300 388 420 384 C580 380 770 330 900 170 L900 514 Z" fill="#33a6d7"/>
    <path d="M214 514 C240 428 310 398 425 394 C585 390 775 345 900 200 L900 514 Z" fill="#0255a3"/>
    <path d="M232 514 C258 440 325 412 435 408 C595 404 785 362 900 232 L900 514 Z" fill="url(#waveFill)"/>
  </svg>

  <div class="identity">
    <p class="identity__title">TITLE</p>
    <p class="identity__company">COMPANY NAME</p>
  </div>

  <svg class="timeline" viewBox="0 0 900 514" aria-hidden="true">
    <line x1="560" y1="0" x2="560" y2="350" stroke="#0255a3" stroke-width="7"/>
    <g fill="#0255a3">
      <circle cx="560" cy="95" r="24"/>
      <circle cx="560" cy="180" r="24"/>
      <circle cx="560" cy="265" r="24"/>
      <circle cx="560" cy="350" r="24"/>
    </g>
    <!-- phone -->
    <path d="M551 86 c2-2 5 0 6 2 l2 4 c1 2-1 3-2 4 c2 4 4 6 8 8 c1-1 2-3 4-2 l4 2 c2 1 4 4 2 6 c-3 3-8 4-14 0 c-5-3-9-7-12-12 c-3-6-2-10 2-12z" fill="#111"/>
    <!-- envelope -->
    <rect x="547" y="171" width="26" height="18" fill="#111"/>
    <polyline points="547,171 560,182 573,171" fill="none" stroke="#0255a3" stroke-width="2"/>
    <!-- pin -->
    <path d="M560 251 a9 9 0 0 1 9 9 c0 7-9 17-9 17 s-9-10-9-17 a9 9 0 0 1 9-9z" fill="#111"/>
    <circle cx="560" cy="260" r="3.5" fill="#0255a3"/>
    <!-- globe -->
    <g fill="none" stroke="#111" stroke-width="2">
      <circle cx="560" cy="350" r="13"/>
      <ellipse cx="560" cy="350" rx="6" ry="13"/>
      <line x1="547" y1="350" x2="573" y2="350"/>
      <line x1="549" y1="343" x2="571" y2="343"/>
      <line x1="549" y1="357" x2="571" y2="357"/>
    </g>
  </svg>

  <p class="contact" style="left:600px; top:62px;">1800 000 000 000</p>
  <p class="contact" style="left:740px; top:20px;">1800 000 000 000</p>
  <p class="contact" style="left:600px; top:170px;">info@pramora.com.au</p>
  <p class="contact" style="left:600px; top:255px;">Location</p>
  <p class="contact" style="left:600px; top:340px;">Website</p>
</section>

</body>
</html>
```